Lanterns and lemonades - fun, casual event near the beach to raise money for needy families

We are seeking a logo, invitation and save the date for our charity event called "Lanterns and Lemonades" set to occur on Dec 1,2017. We want to use the logo on letterhead, social media, etc.

Officially formed in 1955, our all-volunteer organization fundraises to offer a unique service in our area - providing one-time emergency assistance for those experiencing an unexpected temporary downturn.

Referrals come to us from governmental or private social service organizations as well as churches and temples. We work with social service professionals who have developed plans with their clients so they can get back on their feet after receiving our assistance. We have developed an extensive network of professionals in the community upon whom we can rely - and who in turn depend upon us for stopgap funding.

We are there when all other alternatives have been exhausted and immediate help is needed. We provide emergency assistance to those with a recovery plan in place and a goal of financial stability and thereby improving the quality of life for children, the elderly, single men and women and families in our area.

Target Market(s)

Age 35-65 affluent couples

Industry/Entity Type

Charity

Font styles to use
Decorative
Script

Colors

Designer to choose colors to be used in the design.

Requirements
Must have
• Image of margaritas and holiday themeno specific mention of "Christmas" no specific mention of "Christmas"
Nice to have
• Maybe beach-ish or water theme. Event will be at a rooftop bar along the beach.
Should not have
• no specific mention of "Christmas"

```html
<!DOCTYPE html>
<html lang="en">
<head>
<meta charset="utf-8">
<title>Lanterns and Lemonades – Invitation</title>
<link rel="stylesheet" href="https://fonts.googleapis.com/css2?family=Bodoni+Moda:wght@400;600&family=Sorts+Mill+Goudy&display=swap">
<style>
  :root {
    --paper: #ffffff;
    --ink: #111111;
    --festive-red: #d9252b;
    --lime: #b0d57e;
    --lime-dot: #8cc63f;
    --rsvp-green: #3aa843;
    --rule: #222222;
  }
  html, body {
    margin: 0;
    padding: 0;
    overflow: hidden;
    background: var(--paper);
  }
  .invitation {
    position: relative;
    width: 800px;
    height: 1200px;
    overflow: hidden;
    background: var(--paper);
    font-family: "Bodoni Moda", "Didot", serif;
  }
  .frame { position: absolute; top: 0; left: 0; }

  .invite-lead {
    position: absolute;
    left: 51px;
    top: 42px;
    margin: 0;
    color: var(--festive-red);
    font-weight: 600;
    font-size: 41px;
    line-height: 53px;
    letter-spacing: 1.5px;
  }

  .event-name {
    position: absolute;
    left: 0;
    top: 0;
    margin: 0;
    color: var(--ink);
    font-weight: 600;
  }
  .event-name span { position: absolute; white-space: nowrap; line-height: 1; }
  .event-name .word-one { left: 78px; top: 280px; font-size: 104px; }
  .event-name .word-and { left: 300px; top: 402px; font-size: 60px; }
  .event-name .word-two { left: 220px; top: 478px; font-size: 92px; }
  .name-dot {
    position: absolute;
    left: 606px;
    top: 326px;
    width: 80px;
    height: 80px;
    border-radius: 50%;
    background: var(--lime-dot);
  }

  .event-details {
    position: absolute;
    right: 52px;
    top: 660px;
    margin: 0;
    text-align: right;
    color: var(--festive-red);
    font-weight: 600;
    font-size: 37px;
    line-height: 44px;
    letter-spacing: 1px;
  }
  .event-details .time { display: block; margin-top: 6px; font-size: 40px; }

  .info-panel {
    position: absolute;
    left: 94px;
    top: 786px;
    width: 286px;
    height: 414px;
    background: var(--lime);
  }
  .info-panel p {
    margin: 0;
    padding: 52px 0 0 36px;
    font-family: "Sorts Mill Goudy", "Garamond", serif;
    color: var(--ink);
    font-size: 31px;
    line-height: 40px;
    white-space: nowrap;
  }

  .rsvp {
    position: absolute;
    right: 66px;
    top: 1004px;
    margin: 0;
    text-align: right;
    color: var(--rsvp-green);
    font-weight: 400;
    font-size: 33px;
    line-height: 41px;
  }
</style>
</head>
<body>
  <main class="invitation">
    <svg class="frame" width="800" height="1200" viewBox="0 0 800 1200" aria-hidden="true">
      <g stroke="var(--rule)" stroke-width="1.5" fill="none">
        <line x1="572" y1="50" x2="751" y2="50"/>
        <line x1="750" y1="50" x2="750" y2="648"/>
        <line x1="750" y1="896" x2="750" y2="1149"/>
        <line x1="392" y1="1148" x2="751" y2="1148"/>
        <line x1="49" y1="1148" x2="94" y2="1148"/>
        <line x1="50" y1="204" x2="50" y2="1149"/>
      </g>
    </svg>

    <p class="invite-lead">You are invited to attend<br>a holiday event<br>involving...</p>

    <h1 class="event-name" aria-label="Lanterns and Lemonades">
      <span class="word-one">Lanterns</span>
      <span class="word-and">and</span>
      <span class="word-two">Lemonades</span>
    </h1>
    <div class="name-dot" aria-hidden="true"></div>

    <p class="event-details">
      Friday, December 1. 2017<br>
      Seabreeze Hotel<br>
      Whatever, Fl<br>
      Rooftop Bar
      <span class="time">7:00 p.m</span>
    </p>

    <aside class="info-panel">
      <p>A little<br>information here<br>about the event<br>or charity affair.<br>Dress code or<br>name of hosts</p>
    </aside>

    <p class="rsvp">RSVP<br>Maren Holloway<br>at 555.013.2468</p>
  </main>
</body>
</html>
```